K7 Electrical Services Ltd Web design

I require a web site for my new electrical contracting company. We are customer service orientated. Offering high value electrical installations, design and maintenance. Focused on custom residential and commercial upgrading. Lighting design and application are paramount in our company's services. Industry leading product use and integration are always on the forefront with our customer client services. As well as energy efficiency.

Target Market(s)

Homebuilders, General Contractors, Property management companies, clients, individuals,

Industry/Entity Type

Electric Company

Coding

Coded - Design and coding required

Number of Pages Required

3 page

Requirements
Must have
• Classic, modern, edgy but not trendy . Appeals to the masse.
• 3 page
• home page
• about page
• gallery page
• ability to contact from the webiste
Nice to have
• open to all types of designs that are relative to the construction industry.
• Black, Grey, metallic ice blue and deep purple colours from the logo.
Should not have
• anything cheesy with cartoon light bulb images.

```html
<!DOCTYPE html>
<html lang="en">
<head>
<meta charset="utf-8">
<title>K7 Electrical Services Ltd</title>
<link href="https://fonts.googleapis.com/css2?family=Open+Sans:ital,wght@0,300;0,400;0,600;0,700;1,400&display=swap" rel="stylesheet">
<style>
:root{
  --purple:#5a2a87;
  --purple-dark:#47206d;
  --purple-soft:#8d6bb3;
  --ink:#2c2c3a;
  --text:#6b6b7b;
  --muted:#9a9aa8;
  --band:#f3f3f7;
  --white:#ffffff;
  --line:#e3e3ea;
}
*{margin:0;padding:0;box-sizing:border-box}
html,body{width:1200px;height:3838px;overflow:hidden}
body{font-family:"Open Sans",Helvetica,Arial,sans-serif;color:var(--text);background:var(--white);position:relative}
.section{position:absolute;left:0;width:1200px}
.abs{position:absolute}
.label{font-size:15px;color:var(--purple-soft);font-weight:400}
.heading{font-size:30px;color:var(--purple-dark);font-weight:400}
.copy{font-size:13px;line-height:20px;color:var(--text)}

/* header */
.site-header{top:0;height:102px;background:var(--white);box-shadow:0 1px 6px rgba(0,0,0,.06)}
.topbar{position:absolute;right:0;top:0;width:820px;height:30px;background:var(--purple);clip-path:polygon(28px 0,100% 0,100% 100%,0 100%);display:flex;justify-content:flex-end;align-items:center;gap:26px;padding-right:40px;font-size:12px;color:var(--white)}
.topbar span{display:flex;align-items:center;gap:7px}
.logo{position:absolute;left:51px;top:30px;display:flex;align-items:center;gap:12px}
.logo-mark{width:40px;height:40px;background:var(--purple)}
.logo-name{font-size:22px;font-weight:600;color:var(--purple);line-height:1.1}
.nav{position:absolute;right:50px;top:56px;display:flex;gap:40px;font-size:14px;color:var(--ink)}
.nav .active{color:var(--purple)}

/* hero */
.hero{top:102px;height:486px;background:linear-gradient(110deg,#c9ccd2 0%,#a9aeb8 38%,#6c6f80 52%,#2d2f44 70%,#3a3345 100%)}
.hero-badge{position:absolute;left:525px;top:154px;width:230px;height:230px;border-radius:50%;background:rgba(90,42,135,.82);color:var(--white);text-align:center;padding-top:48px;font-size:25px;line-height:38px;letter-spacing:1px}
.hero-badge strong{font-weight:700;font-size:30px}

/* about */
.about{top:588px;height:397px}
.btn{position:absolute;height:38px;border-radius:19px;font-size:13px;display:flex;align-items:center;justify-content:center}
.btn-primary{background:var(--purple);color:var(--white);font-weight:600}
.btn-ghost{border:1px solid var(--line);color:var(--text)}
.about-photo{position:absolute;left:709px;top:72px;width:399px;height:269px;background:linear-gradient(135deg,#e9ebf0,#bcc3d2 60%,#3b55a0);box-shadow:0 4px 18px rgba(90,42,135,.25)}

/* services */
.services{top:985px;height:690px;background:var(--band)}
.svc-item{position:absolute;left:51px;width:276px;height:72px;display:flex;align-items:center;gap:16px;padding-left:26px;font-size:13px;color:var(--purple-soft)}
.svc-item.active{background:var(--white);color:var(--ink);font-weight:600;box-shadow:0 2px 8px rgba(0,0,0,.05)}
.svc-dot{width:42px;height:42px;border-radius:50%;background:#9a9aa6}
.svc-photo{position:absolute;top:524px;width:197px;height:103px}

/* features */
.features{top:1675px;height:627px;text-align:center}
.feature{position:absolute;width:260px;text-align:left}
.feature h3{font-size:17px;color:var(--ink);font-weight:600;margin:22px 0 12px}
.feature p{font-size:12px;line-height:18px;color:var(--muted)}

/* testimonials */
.testimonials{top:2302px;height:486px;background:var(--band)}
.quote-card{position:absolute;top:251px;width:352px;height:174px;background:var(--white);padding:24px 22px}
.quote-avatar{position:absolute;left:22px;top:26px;width:50px;height:50px;border-radius:50%;background:#c9b7a6}
.quote-text{margin-left:74px;font-size:12px;line-height:17px;font-style:italic;color:var(--muted)}
.quote-name{margin:14px 0 0 74px;font-size:12px;color:var(--ink)}

/* gallery */
.gallery{top:2788px;height:583px}
.gallery-grid{position:absolute;top:210px;left:0;display:grid;grid-template-columns:repeat(5,240px);grid-template-rows:repeat(2,186px);gap:1px;width:1204px}
.tile{background:linear-gradient(160deg,#8fa3c2,#5b6470 55%,#6b7d4a)}

/* contact */
.contact{top:3371px;height:389px;background:var(--band);border-top:5px solid var(--purple)}
.contact h4{font-size:17px;color:var(--ink);font-weight:600}
.field{position:absolute;height:32px;background:var(--white);border:1px solid var(--line);border-radius:3px;font-size:11px;color:var(--muted);padding:8px 10px}
.map{position:absolute;left:333px;top:108px;width:537px;height:225px;background:linear-gradient(135deg,#d9e6ef,#eceae3 50%,#c7dcc0)}
.social{display:flex;gap:14px;position:absolute;left:895px;top:312px}
.social span{width:26px;height:26px;border-radius:50%;background:var(--purple)}
.contact-list p{font-size:12px;line-height:18px;color:var(--text);margin-bottom:14px}

.site-footer{top:3760px;height:78px;background:var(--purple);color:var(--white);font-size:12px;display:flex;align-items:center;justify-content:center}
</style>
</head>
<body>

<header class="section site-header">
  <div class="topbar">
    <span><svg width="12" height="12" viewBox="0 0 24 24" fill="#fff"><path d="M6.6 10.8a15 15 0 0 0 6.6 6.6l2.2-2.2a1 1 0 0 1 1-.25 11.4 11.4 0 0 0 3.6.6 1 1 0 0 1 1 1V20a1 1 0 0 1-1 1A17 17 0 0 1 3 4a1 1 0 0 1 1-1h3.5a1 1 0 0 1 1 1c0 1.25.2 2.45.6 3.6a1 1 0 0 1-.25 1z"/></svg>+1 800 555 01 47</span>
    <span><svg width="13" height="10" viewBox="0 0 26 20" fill="#fff"><rect width="26" height="20" rx="2"/><path d="M1 2l12 9 12-9" stroke="#5a2a87" stroke-width="2" fill="none"/></svg>hello@k7electrical.example</span>
  </div>
  <div class="logo"><span class="logo-mark"></span><span class="logo-name">K7 Electrical Services</span></div>
  <nav class="nav"><span class="active">HOME</span><span>ABOUT US</span><span>OUR SERVICES</span><span>GALLERY</span><span>CONTACT US</span></nav>
</header>

<section class="section hero" role="img" aria-label="Lit empty warehouse interior beside a modern glass house at dusk">
  <div class="hero-badge">DO YOU<br><strong>NEED</strong> A<br>ELECTRICIAN</div>
</section>

<section class="section about">
  <div class="abs label" style="left:51px;top:30px">About Us</div>
  <h2 class="abs heading" style="left:51px;top:56px">Who we are ?</h2>
  <div class="abs copy" style="left:51px;top:112px;width:500px">
    <p>We have many years of foreign experience on projects for affluent clients.<br>We know, how to provide high quality work. While on the job site, we do not perceive</p>
    <p style="margin-top:14px">only our profession, but we see each project as a teamwork, where all traders have tobe taken in to consideration. That's how we achieve perfect result and place all electrical components exactly into desired location or detail.</p>
    <p style="margin-top:14px">You can rely on us with electrical installations for you or for your dear clients.</p>
  </div>
  <div class="btn btn-primary" style="left:51px;top:319px;width:160px">Contact Us</div>
  <div class="btn btn-ghost" style="left:248px;top:319px;width:156px">Read More</div>
  <div class="about-photo" role="img" aria-label="Electrician in overalls holding a clipboard beside a water heater"></div>
</section>

<section class="section services">
  <div class="abs label" style="left:51px;top:49px">Services</div>
  <h2 class="abs heading" style="left:51px;top:80px">What we do ?</h2>
  <p class="abs copy" style="left:51px;top:140px;width:340px">We are company specialize in quality electrical installations in private houses, apartments and commercial spaces.</p>

  <div class="svc-item active" style="top:231px"><span class="svc-dot" role="img" aria-label="Electric installation thumbnail" style="background:#6a5c7e"></span>Electric Installations</div>
  <div class="svc-item" style="top:319px"><span class="svc-dot" role="img" aria-label="Smart home panel thumbnail"></span>Smart Home Installations</div>
  <div class="svc-item" style="top:396px"><span class="svc-dot" role="img" aria-label="Security camera thumbnail"></span>Camera systems</div>
  <div class="svc-item" style="top:473px"><span class="svc-dot" role="img" aria-label="Alarm keypad thumbnail" style="background:#a38e86"></span>Alarms</div>
  <div class="svc-item" style="top:550px"><span class="svc-dot" role="img" aria-label="Green energy landscape thumbnail" style="background:linear-gradient(#3d7fd0,#5aa43d)"></span>Energy efficiency</div>

  <h3 class="abs" style="left:409px;top:258px;font-size:17px;font-weight:400;color:var(--ink)">Electric Installations</h3>
  <div class="abs copy" style="left:409px;top:306px;width:640px">
    <p>Lorem ipsum dolor sit amet, consectetur adipiscing elit, sed do eiusmod tempor incididunt ut labore et dolore magna aliqua. Ut enim ad minim veniam, quis nostrud exercitation ullamco laboris nisi ut aliquip ex ea commodo consequat. Duis aute irure dolor in reprehenderit in voluptate velit esse cillum dolore eu.</p>
    <p style="margin-top:8px">Lorem ipsum dolor sit amet, consectetur adipiscing elit, sed do eiusmod tempor incididunt ut labore et dolore magna aliqua. Ut enim ad minim veniam, quis nostrud exercitation ullamco laboris nisi ut.</p>
  </div>
  <div class="abs" style="left:409px;top:454px;font-size:13px;font-weight:600;color:var(--purple)">Details ›</div>
  <div class="svc-photo" style="left:412px;background:linear-gradient(135deg,#e7e2d8,#c9a64a)" role="img" aria-label="Electrician wiring a socket"></div>
  <div class="svc-photo" style="left:640px;background:linear-gradient(135deg,#d8d8dc,#b03a3a 60%,#777)" role="img" aria-label="Testing a breaker panel"></div>
  <div class="svc-photo" style="left:867px;background:linear-gradient(135deg,#e4ded6,#8a7a6c)" role="img" aria-label="Hands working on a fuse board"></div>
</section>

<section class="section features">
  <div class="abs label" style="left:0;width:1200px;top:30px">Features</div>
  <h2 class="abs heading" style="left:0;width:1200px;top:60px">Why choose us ?</h2>
  <p class="abs copy" style="left:430px;width:340px;top:126px">We have many years of foreign experience on projects for effluent clients. We know, how to provide high quality work.</p>

  <div class="feature" style="left:192px;top:220px">
    <svg width="60" height="60" viewBox="0 0 48 48" fill="none" stroke="#5a2a87" stroke-width="2"><circle cx="24" cy="24" r="16"/><path d="M24 14v10l7 5"/></svg>
    <h3>Arrival on time</h3><p>Sed ut perspiciatis unde omnis iste natus error sit voluptate accusantium doloremqu.</p>
  </div>
  <div class="feature" style="left:476px;top:220px">
    <svg width="60" height="60" viewBox="0 0 48 48" fill="none" stroke="#5a2a87" stroke-width="2"><path d="M10 38l18-18M30 8a8 8 0 0 0-4 10l4 4a8 8 0 0 0 10-4l-5 1-4-4 1-5z"/><path d="M10 10l28 28M8 12l4-4"/></svg>
    <h3>Professional equipment</h3><p>Nemo qui enim ipsam voluptatem quia voluptas sit aspernatur aut odit aut fugit.</p>
  </div>
  <div class="feature" style="left:757px;top:220px">
    <svg width="60" height="60" viewBox="0 0 48 48" fill="none" stroke="#5a2a87" stroke-width="2"><path d="M24 8l4 8 9 1-7 6 2 9-8-5-8 5 2-9-7-6 9-1z"/><path d="M12 36h24v6H12z"/></svg>
    <h3>Proposition of best solution</h3><p>Sed ut perspiciatis unde omnis iste natus error sit voluptatem accusantium quido et.</p>
  </div>
  <div class="feature" style="left:192px;top:420px">
    <svg width="60" height="60" viewBox="0 0 48 48" fill="none" stroke="#5a2a87" stroke-width="2"><path d="M4 24s8-12 20-12 20 12 20 12-8 12-20 12S4 24 4 24z"/><circle cx="24" cy="24" r="6"/></svg>
    <h3>Great sense for detail</h3><p>Sed ut perspiciatis unde omnis iste natus error sit voluptate accusantium doloremqu.</p>
  </div>
  <div class="feature" style="left:476px;top:420px">
    <svg width="60" height="60" viewBox="0 0 48 48" fill="none" stroke="#5a2a87" stroke-width="2"><circle cx="24" cy="24" r="15"/><path d="M24 15l3 6 6 1-4.5 4 1 6-5.5-3-5.5 3 1-6-4.5-4 6-1z"/></svg>
    <h3>Professional approach</h3><p>Nemo qui enim ipsam voluptatem quia voluptas sit aspernatur aut odit aut fugit.</p>
  </div>
  <div class="feature" style="left:757px;top:420px">
    <svg width="60" height="60" viewBox="0 0 48 48" fill="none" stroke="#5a2a87" stroke-width="2"><rect x="12" y="6" width="24" height="36" rx="2"/><path d="M17 15h14M17 22h14M17 29h9"/></svg>
    <h3>Compliance of your plans</h3><p>Sed ut perspiciatis unde omnis iste natus error sit voluptatem accusantium quido et.</p>
  </div>
</section>

<section class="section testimonials">
  <div class="abs label" style="left:51px;top:56px">Testimonials</div>
  <h2 class="abs heading" style="left:51px;top:86px">What Our Client Says ?</h2>
  <p class="abs copy" style="left:51px;top:150px;width:360px">What our clients say about our services and how we helped us and make them life better than before</p>

  <div class="quote-card" style="left:51px">
    <div class="quote-avatar" role="img" aria-label="Client portrait"></div>
    <p class="quote-text">Duis aute irure dolor in reprehenderit in voluptate velit esse cillum dolore eu fugiat nulla pariatur. Excepteur sint occaecat cupidatat non proident, sunt in culpa qui officia deserunt mollit.</p>
    <p class="quote-name">Owen Marsh, Operations Manager</p>
  </div>
  <div class="quote-card" style="left:425px">
    <div class="quote-avatar" role="img" aria-label="Client portrait" style="background:#b89a7c"></div>
    <p class="quote-text">Provident, similique sunt in culpa qui officia deserunt mollitia animi, id est laborum et dolorum fuga. Et harum quidem rerum facilis est et expedita distinctio. Nam libero tempore, cum soluta nobis.</p>
    <p class="quote-name">Clara Benton, Creative Designer</p>
  </div>
  <div class="quote-card" style="left:796px">
    <div class="quote-avatar" role="img" aria-label="Client portrait" style="background:#8c7466"></div>
    <p class="quote-text">Duis aute irure dolor in reprehenderit in voluptate velit esse cillum dolore eu fugiat nulla pariatur. Excepteur sint occaecat cupidatat non proident, sunt in culpa qui officia deserunt mollit.</p>
    <p class="quote-name">Nina Hollis, Manager</p>
  </div>
</section>

<section class="section gallery">
  <div class="abs label" style="left:51px;top:38px">Gallery</div>
  <h2 class="abs heading" style="left:51px;top:70px">Are an exension of our team and success</h2>
  <p class="abs copy" style="left:51px;top:132px;width:230px">Do you have any question or are you looking for Installers?</p>
  <div class="gallery-grid">
    <div class="tile" role="img" aria-label="Modern house at dusk"></div>
    <div class="tile" role="img" aria-label="Lit villa at sunset" style="background:linear-gradient(160deg,#c98d5e,#4b4a52 60%,#3e5a2e)"></div>
    <div class="tile" role="img" aria-label="Contemporary two-storey home" style="background:linear-gradient(160deg,#a8b5c8,#6f6f74)"></div>
    <div class="tile" role="img" aria-label="Warm lit interior" style="background:linear-gradient(160deg,#c58a4e,#6d4a2c)"></div>
    <div class="tile" role="img" aria-label="Suburban house with lawn" style="background:linear-gradient(160deg,#8fb0d8,#7d7d82 55%,#6f9448)"></div>
    <div class="tile" role="img" aria-label="House with garden path" style="background:linear-gradient(160deg,#9ec0e4,#8a8a8f 55%,#5f8d3e)"></div>
    <div class="tile" role="img" aria-label="Chalet in snow" style="background:linear-gradient(160deg,#3b4f7c,#b7a48a 55%,#dfe6ee)"></div>
    <div class="tile" role="img" aria-label="Family home among trees" style="background:linear-gradient(160deg,#7ea8d6,#c9b59a 50%,#4f7d35)"></div>
    <div class="tile" role="img" aria-label="Timber-clad house" style="background:linear-gradient(160deg,#a7c3e0,#8a6a4a 55%,#5a7e3a)"></div>
    <div class="tile" role="img" aria-label="Villa with pool" style="background:linear-gradient(160deg,#8db3de,#d8d4cc 55%,#3f8fc4)"></div>
  </div>
</section>

<section class="section contact">
  <h4 class="abs" style="left:51px;top:72px">Feel Free to Mail</h4>
  <div class="field" style="left:51px;top:118px;width:118px">Name *</div>
  <div class="field" style="left:186px;top:118px;width:118px">Email *</div>
  <div class="field" style="left:51px;top:165px;width:253px">Subject</div>
  <div class="field" style="left:51px;top:212px;width:253px;height:72px">Write Your Message Here...</div>
  <div class="btn btn-primary" style="left:51px;top:305px;width:140px;height:30px;font-size:12px">SEND MESSAGE</div>

  <h4 class="abs" style="left:333px;width:537px;top:72px;text-align:center">Headquarters</h4>
  <div class="map" role="img" aria-label="Street map showing the office location at the harbour"></div>

  <h4 class="abs" style="left:895px;top:72px">Contact Info</h4>
  <div class="abs contact-list" style="left:895px;top:110px;width:250px">
    <p>Our staff is available to you from 9AM until 5PM on weekdays.</p>
    <p>Phone: +1 (500) 555 01 88</p>
    <p>Office: Harbor Point Plaza</p>
    <p>Email: hello@k7electrical.example</p>
  </div>
  <h4 class="abs" style="left:895px;top:276px">Follow Us on</h4>
  <div class="social"><span></span><span></span><span></span><span></span><span></span></div>
</section>

<footer class="section site-footer">© 2018 All Rights Reserved by K7 Electrical Services Ltd</footer>

</body>
</html>
```